Brisket Electrical Business Card Design

A Registered Electrical Contractor with +21 years experience backed with advanced electrical and electronics education. The design should appeal to the industrial, commercial and domestic electrical industry. Final design should communicate prompt, diverse, professional service.
Updates

The Business Name is "Brisket Electrical" not brisket Electrical South Eastern Suburbs

Reason: I have committed payment, removed colour limitations and asked for images to be added so designers can have more freedom to capture the audience with the WOW factor. So go for it and show me what you got. GOOD LUCK EVERYONE

Target Market(s)

Target Industrial business sector, domestic faults and repairs.
We cover all electrical faults, power, lighting, installation, control wiring, machines, process lines, appliances, maintenance, compliance testing, overhead cranes, switchboards and more.

Industry/Entity Type

Electronics

Contact Information for Business Card

Brisket Electrical
South Eastern Suburbs
Melbourne, Victoria 3976
0432 519 284
brisketelectrical@mailpost.example
ABN: 48 206 953 172
REC: 37509

Requirements
Must have
• 1 - "REC: 37509" should be at the top righthand corner.
2 - Trade picture to reflect wow factor. e.g Lighning, electrician.
3 - List format:( I will ask you to edit as required if design looks too cluttered)
Industrial, Commercial, Domestic, Manufacturing, Installation, Faults, Maintenance,
Commissioning, Compliance Testing, HV Equipment, Generators, Pumps, Overhead Cranes, Power, Lighting, Appliances, Leads, Process Lines, Control Wiring, Main Control Cubicles, Switchboards, Motor Control, VSD, PLC, Electronics, …
Nice to have
• The letters B and E as a combined shape to be used as a logo
Should not have
• "since 21 Year"

```html
<!DOCTYPE html>
<html lang="en">
<head>
<meta charset="utf-8">
<title>Brisket Electrical – Business Card</title>
<link rel="stylesheet" href="https://fonts.googleapis.com/css2?family=Open+Sans:wdth,wght@75..100,400..800&display=swap">
<style>
  :root {
    --backdrop: #2c3638;
    --green-glow: #d9ffb0;
    --green-bright: #7cf91c;
    --green-main: #5fe010;
    --green-deep: #43c206;
    --ink: #111111;
    --rule: rgba(255, 255, 255, 0.85);
    --photo-light: #e6f2ec;
    --photo-teal: #6fb8b4;
    --photo-green: #8fd86a;
  }

  * { margin: 0; padding: 0; box-sizing: border-box; }

  html, body {
    width: 1200px;
    height: 800px;
    overflow: hidden;
  }

  body {
    background: var(--backdrop);
    font-family: "Open Sans", Arial, sans-serif;
    position: relative;
  }

  .business-card {
    position: absolute;
    left: 100px;
    top: 92px;
    width: 1000px;
    height: 616px;
    overflow: hidden;
    background:
      radial-gradient(ellipse 420px 300px at 260px 20px, var(--green-glow) 0%, rgba(180, 255, 110, 0.55) 35%, rgba(124, 249, 28, 0) 75%),
      linear-gradient(160deg, var(--green-bright) 0%, var(--green-main) 55%, var(--green-deep) 100%);
  }

  .trade-photo {
    position: absolute;
    top: 0;
    right: 0;
    width: 420px;
    height: 100%;
    background:
      radial-gradient(ellipse 160px 200px at 330px 120px, #e8f4d8 0%, rgba(232, 244, 216, 0) 70%),
      linear-gradient(180deg, var(--photo-light) 0%, var(--photo-teal) 45%, var(--photo-green) 75%, var(--photo-light) 100%);
    -webkit-mask-image: linear-gradient(90deg, transparent 0%, rgba(0, 0, 0, 0.55) 30%, #000 60%);
    mask-image: linear-gradient(90deg, transparent 0%, rgba(0, 0, 0, 0.55) 30%, #000 60%);
  }

  .brand {
    position: absolute;
    left: 136px;
    top: 92px;
    display: flex;
    align-items: flex-start;
    gap: 18px;
  }

  .brand-square {
    width: 34px;
    height: 34px;
    background: var(--ink);
    margin-top: 10px;
  }

  .brand-name {
    font-stretch: 75%;
    font-weight: 700;
    font-size: 52px;
    line-height: 1;
    color: var(--ink);
    text-transform: uppercase;
    letter-spacing: -0.5px;
  }

  .licence-top {
    position: absolute;
    left: 533px;
    top: 95px;
    font-size: 27px;
    color: var(--ink);
  }

  .divider {
    position: absolute;
    left: 0;
    top: 364px;
    width: 525px;
    height: 3px;
    background: var(--rule);
  }

  .contact-list {
    position: absolute;
    left: 142px;
    top: 428px;
    list-style: none;
    font-size: 28px;
    line-height: 39px;
    color: var(--ink);
  }
</style>
</head>
<body>
  <section class="business-card">
    <div class="trade-photo" role="img" aria-label="Photo of an electrician's hand testing a switchboard's wiring with a digital multimeter"></div>

    <div class="brand">
      <span class="brand-square"></span>
      <h1 class="brand-name">Brisket<br>Electrical</h1>
    </div>

    <p class="licence-top">REC: 37509</p>

    <div class="divider"></div>

    <ul class="contact-list">
      <li>South Eastern Suburbs 0432 519 284</li>
      <li>brisketelectrical@mailpost.example</li>
      <li>ABN: 48 206 953 172 REC: 37509</li>
    </ul>
  </section>
</body>
</html>
```